business cards

we want our logos on the back
the information on it are on the design I've uploaded
come up with whatever you think is best, we want something professional, sophisticated and sleek.

```html
<!DOCTYPE html>
<html lang="en">
<head>
<meta charset="utf-8">
<title>Kestrel Health and Performance – Business Cards</title>
<link rel="stylesheet" href="https://fonts.googleapis.com/css2?family=Josefin+Sans:wght@400;600&display=swap">
<style>
  :root {
    --backdrop: #3a3a3a;
    --card: #1b1b1b;
    --ink: #ffffff;
    --accent: #4cba3f;
    --muted: #bdbdbd;
  }
  * { box-sizing: border-box; margin: 0; padding: 0; }
  html, body { width: 1200px; height: 895px; overflow: hidden; }
  body {
    background: var(--backdrop);
    font-family: "Josefin Sans", sans-serif;
    color: var(--ink);
  }
  .sheet {
    position: relative;
    width: 1200px;
    height: 895px;
  }
  .card {
    position: absolute;
    left: 290px;
    width: 620px;
    height: 354px;
    background: var(--card);
    border-radius: 18px;
    overflow: hidden;
    box-shadow: 0 10px 30px rgba(0,0,0,0.45);
  }
  .card::after {
    content: "";
    position: absolute;
    left: 0; right: 0; bottom: 0;
    height: 7px;
    background: var(--accent);
  }
  .card--front { top: 46px; }
  .card--back { top: 450px; }

  /* Front */
  .brand {
    position: absolute;
    left: 0; right: 0;
    top: 118px;
    text-align: center;
  }
  .brand__name {
    display: inline-flex;
    align-items: center;
    gap: 14px;
    font-weight: 600;
    font-size: 50px;
    letter-spacing: 14px;
    color: var(--ink);
  }
  .brand__dot {
    width: 16px; height: 16px;
    background: var(--accent);
  }
  .brand__sub {
    margin-top: 10px;
    font-size: 14px;
    font-weight: 600;
    letter-spacing: 9px;
    color: var(--ink);
  }
  .brand__rule {
    width: 400px;
    height: 1px;
    background: var(--muted);
    margin: 8px auto 6px;
  }
  .brand__services {
    font-size: 10px;
    letter-spacing: 1.2px;
    color: var(--accent);
  }

  /* Back */
  .back-brand {
    position: absolute;
    top: 54px; left: 0; right: 0;
    text-align: center;
    font-weight: 600;
    font-size: 30px;
    letter-spacing: 9px;
  }
  .person {
    position: absolute;
    right: 330px;
    top: 168px;
    text-align: right;
  }
  .person__name {
    font-size: 26px;
    color: var(--accent);
    letter-spacing: 1px;
    margin-bottom: 6px;
  }
  .person__role {
    font-size: 17px;
    line-height: 1.3;
  }
  .divider {
    position: absolute;
    left: 310px;
    top: 170px;
    width: 1px;
    height: 130px;
    background: var(--muted);
  }
  .contact {
    position: absolute;
    left: 332px;
    top: 172px;
    list-style: none;
    font-size: 16px;
  }
  .contact__address { margin-bottom: 14px; }
  .contact__row {
    display: flex;
    align-items: center;
    gap: 8px;
    margin-bottom: 7px;
  }
  .contact__icon {
    width: 20px; height: 20px;
    flex: none;
  }
</style>
</head>
<body>
<main class="sheet">

  <section class="card card--front" aria-label="Card front">
    <div class="brand">
      <div class="brand__name"><span class="brand__dot"></span>KESTREL</div>
      <div class="brand__sub">HEALTH AND PERFORMANCE</div>
      <div class="brand__rule"></div>
      <div class="brand__services">PHYSIO · S&amp;C · COACHING · PERSONAL TRAINING · REHAB · RECOVERY</div>
    </div>
  </section>

  <section class="card card--back" aria-label="Card back">
    <div class="back-brand">KESTREL</div>

    <div class="person">
      <p class="person__name">MARCUS DELANEY</p>
      <p class="person__role">Director-</p>
      <p class="person__role">Personal Trainer</p>
      <p class="person__role">Sport Nutritionist</p>
      <p class="person__role">BExSc</p>
    </div>

    <div class="divider"></div>

    <ul class="contact">
      <li class="contact__address">22 Linden Rd, Northvale</li>
      <li class="contact__row">
        <svg class="contact__icon" viewBox="0 0 20 20" aria-hidden="true">
          <circle cx="10" cy="10" r="10" fill="#fff"/>
          <path d="M6 5.5l2 0 1 3-1.3 1a6 6 0 0 0 3 3l1-1.3 3 1v2a1.3 1.3 0 0 1-1.4 1.2A9 9 0 0 1 4.8 6.9 1.3 1.3 0 0 1 6 5.5z" fill="#4cba3f"/>
        </svg>
        03 5550 1827
      </li>
      <li class="contact__row">
        <svg class="contact__icon" viewBox="0 0 20 20" aria-hidden="true">
          <circle cx="10" cy="10" r="10" fill="#fff"/>
          <rect x="7" y="4.5" width="6" height="3.5" fill="#4cba3f"/>
          <rect x="4.5" y="8" width="11" height="5" rx="1" fill="#4cba3f"/>
          <rect x="7" y="11.5" width="6" height="4" fill="#4cba3f" stroke="#fff" stroke-width="0.8"/>
        </svg>
        03 5550 4391
      </li>
      <li class="contact__row">
        <svg class="contact__icon" viewBox="0 0 20 20" aria-hidden="true">
          <circle cx="10" cy="10" r="10" fill="#fff"/>
          <path d="M4 10l12-5-4 11-2.5-4.2z" fill="#4cba3f"/>
        </svg>
        hello@kestrelhealth.example
      </li>
    </ul>
  </section>

</main>
</body>
</html>
```